Bright Meadow Co - labels

I have my logo now so its time to proceed with the labels.
The product is organic juices and smoothies. They will be served in Mason jar's and sold as a premium hand made product into the CBD and outlets around Perth such as yoga studios gyms, cafe's etc. Cleanses to individuals etc.
I have attached the logo and a mock of what I would like to see.
I think the logo and the raw organic, handmade look will work with the Chalkboard design and maybe some bunting to brighten the design.
There is currently approx. 10 Juices and Smoothies to the range so I will need to settle on the design and then have you create a label for each one, once settled on the design.
If you have any questions please let me know.

Text on label:
Raw, Organic, Hand Made, Gluten-Free, Dairy-Free

Juice
Morning Vital Sip
Kale, Apple, Celery, Dandelion, Lemon & Ginger

This product is FRESH. Shake before you enjoy!!!

Label size. highest point for height 70 - 75mm. Length 200mm
I also have more wording and nutritional guide for Australian Standards. I will update soon.
Thank you

    Happy Friday Designers!!!

Well I have just increased the budget to $300. I hope this helps to get some designs coming through. If you need anything else from me please send a message.

I look forward to receiving your designs soon and thank you for working with me on my business. this is such an exciting time for me and you guys are making my dream a reality so thank you for your time.

Regards,

Tamsin

Reason: I have not received many designs so extending for a few more days.

Cafe

• Wording - Hand Made
Raw, Organic, Gluten-Free, Dairy-Free
• A chalk board with Juice or Smoothie - Name and ingredients
Bunting I think will work well with the design of logo and chalk board plus bring some colour.

```html
<!DOCTYPE html>
<html lang="en">
<head>
<meta charset="utf-8">
<title>Bright Meadow Co – Juice Label</title>
<link href="https://fonts.googleapis.com/css2?family=Cabin+Sketch:wght@700&family=Fredericka+the+Great&family=Amatic+SC:wght@700&display=swap" rel="stylesheet">
<style>
  :root {
    --lime: #e3e532;
    --chalk: #2b2b2b;
    --copper: #b9785e;
    --chalk-white: #f2f2f2;
    --tick-red: #e21b23;
    --page: #ffffff;
  }
  html, body { margin: 0; padding: 0; overflow: hidden; background: var(--page); }
  .canvas { position: relative; width: 1200px; height: 1000px; overflow: hidden; }
  .label-shape { position: absolute; inset: 0; }
  .brand-name {
    position: absolute; left: 412px; top: 262px; width: 376px;
    margin: 0; text-align: center; color: var(--chalk-white);
    font-family: "Cabin Sketch", cursive; font-weight: 700;
    font-size: 56px; line-height: 58px; letter-spacing: 1px;
  }
  .product-name {
    position: absolute; left: 300px; top: 586px; width: 600px; margin: 0;
    text-align: center; color: var(--chalk-white); white-space: nowrap;
    font-family: "Fredericka the Great", cursive; font-weight: 400;
    font-size: 49px; line-height: 66px; letter-spacing: 0;
  }
  .ingredients {
    position: absolute; left: 352px; top: 726px; width: 496px; margin: 0;
    text-align: center; color: var(--lime); white-space: nowrap;
    font-family: "Cabin Sketch", cursive; font-weight: 700;
    font-size: 19px; line-height: 30px;
  }
  .claims {
    position: absolute; left: 292px; width: 616px; margin: 0; padding: 0;
    list-style: none; display: flex; justify-content: center; gap: 26px;
    color: var(--chalk-white); font-family: "Cabin Sketch", cursive;
    font-weight: 700; font-size: 21px; line-height: 30px;
  }
  .claims--top { top: 808px; }
  .claims--bottom { top: 852px; gap: 10px; }
  .claims li { display: flex; align-items: center; gap: 4px; }
  .claims svg { width: 30px; height: 30px; }
  .freshness-note {
    position: absolute; left: 292px; top: 910px; width: 616px; margin: 0;
    text-align: center; color: var(--lime); white-space: nowrap;
    font-family: "Amatic SC", cursive; font-weight: 700;
    font-size: 25px; line-height: 30px; font-variant: small-caps;
  }
</style>
</head>
<body>
<main class="canvas">
  <svg class="label-shape" width="1200" height="1000" viewBox="0 0 1200 1000" aria-hidden="true">
    <defs>
      <path id="plaque" d="M328,508 H872 A36 36 0 0 0 908 544 V912 A36 36 0 0 0 872 948 H328 A36 36 0 0 0 292 912 V544 A36 36 0 0 0 328 508 Z"/>
      <symbol id="tick" viewBox="0 0 30 30"><path d="M3 16 L11 25 L27 4" fill="none" stroke="var(--tick-red)" stroke-width="4" stroke-linecap="round" stroke-linejoin="round"/></symbol>
    </defs>
    <g class="outer-band" fill="var(--lime)" stroke="var(--lime)" stroke-width="48" stroke-linejoin="round">
      <circle cx="600" cy="325" r="238"/>
      <use href="#plaque"/>
    </g>
    <g class="inner-rule" fill="var(--copper)" stroke="var(--copper)" stroke-width="10">
      <circle cx="600" cy="325" r="238"/>
      <use href="#plaque"/>
    </g>
    <g class="chalkboard" fill="var(--chalk)">
      <circle cx="600" cy="325" r="236"/>
      <path d="M329,510 H871 A38 38 0 0 0 906 545 V911 A38 38 0 0 0 871 946 H329 A38 38 0 0 0 294 911 V545 A38 38 0 0 0 329 510 Z"/>
    </g>
    <circle class="brand-disc" cx="600" cy="322" r="188" fill="var(--lime)"/>
    <g class="flourishes" fill="none" stroke="var(--chalk-white)" stroke-width="2.5" stroke-linecap="round">
      <path d="M345 680 C400 664 470 666 560 684 C574 687 578 676 566 673"/>
      <path d="M855 680 C800 664 730 666 640 684 C626 687 622 676 634 673"/>
    </g>
    <g class="ribbon" fill="var(--chalk)" stroke="var(--chalk-white)" stroke-width="2.5">
      <path d="M300 730 H360 V790 H300 L318 760 Z"/>
      <path d="M900 730 H840 V790 H900 L882 760 Z"/>
      <rect x="352" y="713" width="496" height="60"/>
      <rect x="358" y="719" width="484" height="48" fill="none" stroke-width="1.2"/>
    </g>
  </svg>

  <h1 class="brand-name">BRIGHT<br>MEADOW CO</h1>
  <h2 class="product-name">MORNING VITAL SIP</h2>
  <p class="ingredients">KALE, APPLE, CELERY, DANDELION, LEMON &amp; GINGER</p>

  <ul class="claims claims--top">
    <li><svg aria-hidden="true"><use href="#tick"/></svg>RAW</li>
    <li><svg aria-hidden="true"><use href="#tick"/></svg>HAND MADE</li>
    <li><svg aria-hidden="true"><use href="#tick"/></svg>ORGANIC</li>
  </ul>
  <ul class="claims claims--bottom">
    <li><svg aria-hidden="true"><use href="#tick"/></svg>DAIRY-FREE</li>
    <li><svg aria-hidden="true"><use href="#tick"/></svg>GLUTEN-FREE</li>
  </ul>

  <p class="freshness-note">This product is FRESH. Shake before you enjoy!!!</p>
</main>
</body>
</html>
```